Billboard For Marek Delvaine

Need a Billboard 8ft. High x 16ft. Long. Ive attached a former billboard and looking for the same thing just updated with:
Summit Lodge Award Logo - 2020, 2022
Pinnacle Ring award Logo - 2022

Thanks.

```html
<!DOCTYPE html>
<html lang="en">
<head>
<meta charset="utf-8">
<title>Billboard – Marek Delvaine</title>
<link rel="stylesheet" href="https://fonts.googleapis.com/css2?family=Jost:ital,wght@0,500;0,600;0,700;1,700;1,800;1,900&family=Oswald:wght@300;400&family=Montserrat:wght@500;600;700&display=swap">
<style>
  :root {
    --backdrop: #3a3839;
    --board-top: #e1e2e4;
    --board-bottom: #ffffff;
    --ink: #0b0b0b;
    --accent: #e31b23;
    --grey-text: #444;
    --photo-light: #d8c0ae;
    --photo-mid: #8a7c86;
    --photo-dark: #2d4c9e;
  }
  * { margin: 0; padding: 0; box-sizing: border-box; }
  html, body { width: 951px; height: 1200px; overflow: hidden; }
  body { background: var(--backdrop); position: relative; font-family: "Jost", sans-serif; }

  .billboard {
    position: absolute; left: 20px; top: 372px; width: 911px; height: 455px;
    background: linear-gradient(180deg, var(--board-top) 0%, var(--board-bottom) 60%);
    overflow: hidden;
    box-shadow: 0 10px 30px rgba(0,0,0,.45);
  }
  .agent-photo {
    position: absolute; left: 0; top: 42px; width: 380px; height: 413px;
    background: linear-gradient(180deg, var(--photo-light) 0%, var(--photo-light) 45%, var(--photo-mid) 62%, var(--photo-dark) 78%);
    border-radius: 46% 46% 0 0 / 30% 30% 0 0;
  }

  .headline {
    position: absolute; font-style: italic; font-weight: 900; font-size: 68px;
    line-height: 1; color: var(--ink); letter-spacing: -0.5px; white-space: nowrap;
  }
  .headline-one { left: 274px; top: 22px; }
  .headline-two { right: 38px; top: 90px; text-align: right; }
  .headline .call { color: var(--accent); margin-left: 20px; }

  .contact-frame { position: absolute; left: 371px; top: 194px; width: 500px; height: 124px; }
  .agent-name {
    position: absolute; left: 371px; width: 500px; top: 172px; text-align: center;
    font-weight: 600; font-size: 42px; line-height: 1; color: var(--ink); letter-spacing: -0.5px;
  }
  .agent-role {
    position: absolute; left: 371px; width: 500px; top: 220px; text-align: center;
    font-family: "Montserrat", sans-serif; font-weight: 600; font-size: 13px; letter-spacing: 4px; color: var(--ink);
  }
  .agent-phone {
    position: absolute; left: 371px; width: 500px; top: 238px; text-align: center;
    font-weight: 600; font-size: 68px; line-height: 1; color: var(--accent); letter-spacing: -1px;
  }
  .tagline {
    position: absolute; left: 371px; width: 500px; top: 328px; text-align: center;
    font-weight: 700; font-size: 24px; color: var(--ink); white-space: nowrap;
  }
  .tagline em { color: var(--accent); font-weight: 800; }

  .credentials { position: absolute; left: 0; top: 0; width: 100%; height: 100%; pointer-events: none; }
  .badge-round { position: absolute; border-radius: 50%; }
  .badge-lodge { left: 382px; top: 382px; width: 56px; height: 56px; border: 2px solid var(--ink); background: #fff; }
  .badge-lodge::after {
    content: ""; position: absolute; left: 8px; top: 8px; width: 36px; height: 36px; border-radius: 50%; background: var(--ink);
  }
  .badge-ring { left: 545px; top: 392px; width: 34px; height: 34px; background: var(--ink); }

  .award { position: absolute; font-family: "Oswald", sans-serif; color: var(--ink); line-height: 1; }
  .award .issuer { font-family: "Montserrat", sans-serif; font-weight: 500; font-size: 7px; color: var(--grey-text); letter-spacing: .3px; display: block; margin-bottom: 2px; }
  .award .title { font-weight: 400; font-size: 17px; display: block; transform: scaleX(.82); transform-origin: left; white-space: nowrap; }
  .award .years { font-family: "Montserrat", sans-serif; font-size: 6px; font-weight: 600; }
  .award-lodge { left: 447px; top: 389px; }
  .award-ring { left: 585px; top: 387px; }
  .award-ring .title { font-weight: 300; color: #222; }

  .brokerage { position: absolute; left: 710px; top: 384px; width: 106px; }
  .brokerage .name {
    display: block; font-family: "Montserrat", sans-serif; font-weight: 700; font-size: 12px;
    color: var(--accent); letter-spacing: .2px; border-top: 4px solid var(--accent); padding-top: 3px; white-space: nowrap;
  }
  .brokerage .office {
    display: block; margin-top: 8px; font-family: "Montserrat", sans-serif; font-weight: 600; font-size: 7px; color: #222; line-height: 1.3;
  }
  .brokerage .office small { font-size: 4.5px; font-weight: 500; }

  .social { position: absolute; left: 826px; top: 404px; font-family: "Montserrat", sans-serif; font-weight: 700; font-size: 9px; color: var(--accent); }
</style>
</head>
<body>
  <section class="billboard">
    <div class="agent-photo" role="img" aria-label="Portrait of Marek Delvaine, sales representative, in a blue shirt and patterned tie"></div>

    <h1 class="headline headline-one">BUYING OR</h1>
    <p class="headline headline-two">SELLING?<span class="call">CALL</span></p>

    <svg class="contact-frame" viewBox="0 0 500 124" aria-hidden="true">
      <path d="M45 2 H14 Q2 2 2 14 V110 Q2 122 14 122 H486 Q498 122 498 110 V14 Q498 2 486 2 H455"
            fill="none" stroke="#e31b23" stroke-width="2.6"/>
    </svg>
    <h2 class="agent-name">MAREK DELVAINE</h2>
    <p class="agent-role">SALES REPRESENTATIVE</p>
    <p class="agent-phone">555.010 .4821</p>
    <p class="tagline">FOCUSED, DRIVEN, AND <em>EXPERIENCED!</em></p>

    <div class="credentials">
      <span class="badge-round badge-lodge"></span>
      <div class="award award-lodge">
        <span class="issuer">CROWN HEARTH</span>
        <span class="title">SUMMIT LODGE</span>
        <span class="years">NATIONAL TOP 1% · 2020 | 2022</span>
      </div>

      <span class="badge-round badge-ring"></span>
      <div class="award award-ring">
        <span class="issuer">CROWN HEARTH</span>
        <span class="title">PINNACLE RING</span>
        <span class="title">AWARD 2022</span>
      </div>

      <div class="brokerage">
        <span class="name">CROWN HEARTH</span>
        <span class="office">ALDER &amp; PARTNERS,<br>BROKERAGE | <small>INDEPENDENTLY OWNED</small></span>
      </div>

      <span class="social">@marekhomes</span>
    </div>
  </section>
</body>
</html>
```